Business Card design for Recruiter providing Recruitment Staff Augmentation services

I need a double sided business card. I have used Zek to print cards in the past and really like their quality. I have a logo but need to change the tagline that is part of the graphic.

The tagline currently reads and Connnecting people with careers - but it should be removed.

The back should look like a notecard for writing a to do list with the first to-do Augment Recruiting Staff

```html
<!DOCTYPE html>
<html lang="en">
<head>
<meta charset="utf-8">
<title>Talent Forge business card</title>
<link rel="stylesheet" href="https://fonts.googleapis.com/css2?family=Questrial&display=swap">
<style>
  :root {
    --navy: #1d4466;
    --orange: #e2643a;
    --paper: #ffffff;
    --paper-back: #f1f1f1;
    --stage: #e4e2de;
    --muted: #3a5673;
  }
  * { box-sizing: border-box; margin: 0; padding: 0; }
  html, body { width: 1200px; height: 1023px; overflow: hidden; }
  body {
    background: var(--stage);
    font-family: "Questrial", "Century Gothic", sans-serif;
    color: var(--navy);
    position: relative;
  }
  .card {
    position: absolute;
    left: 320px;
    width: 560px;
    height: 320px;
    box-shadow: 0 6px 18px rgba(0,0,0,0.18);
  }
  .card-front { top: 120px; background: var(--paper); }
  .card-back { top: 560px; background: var(--paper-back); }

  .brand {
    position: absolute;
    display: flex;
    align-items: center;
    gap: 10px;
  }
  .brand-dot {
    width: 22px; height: 22px;
    border-radius: 50%;
    background: var(--orange);
  }
  .brand-name {
    font-size: 30px;
    letter-spacing: 0.5px;
    color: var(--navy);
    text-transform: uppercase;
  }
  .card-front .brand { left: 34px; top: 34px; }
  .card-back .brand { left: 34px; top: 30px; }

  .holder {
    position: absolute;
    right: 34px;
    top: 40px;
    text-align: right;
  }
  .holder-name { font-size: 19px; color: var(--orange); }
  .holder-rule {
    position: absolute;
    left: 110px; right: 34px; top: 126px;
    height: 2px;
    background: var(--navy);
  }
  .holder-title {
    position: absolute;
    right: 34px; top: 134px;
    font-size: 13px;
    color: var(--navy);
  }
  .address {
    position: absolute;
    right: 34px; top: 178px;
    width: 150px;
    text-align: right;
    font-size: 12px;
    line-height: 1.4;
    color: var(--muted);
  }
  .contact {
    position: absolute;
    left: 34px; bottom: 30px;
    list-style: none;
    font-size: 13px;
    line-height: 1.45;
    color: var(--navy);
  }
  .contact li { display: flex; align-items: center; gap: 7px; }
  .contact svg { width: 11px; height: 11px; fill: var(--orange); }

  .todo-lines {
    position: absolute;
    left: 34px; right: 34px; top: 100px;
    list-style: none;
  }
  .todo-lines li {
    height: 42px;
    border-bottom: 2px solid var(--navy);
  }
</style>
</head>
<body>
  <section class="card card-front" aria-label="Card front">
    <div class="brand">
      <span class="brand-dot"></span>
      <span class="brand-name">Talent Forge</span>
    </div>
    <div class="holder">
      <p class="holder-name">Dana Whitfield, SPHR</p>
    </div>
    <div class="holder-rule"></div>
    <p class="holder-title">Managing Director</p>
    <p class="address">Here your company or home address</p>
    <ul class="contact">
      <li><svg viewBox="0 0 12 12"><path d="M2 1l2.5 0 1 3-1.5 1a6 6 0 0 0 3 3l1-1.5 3 1V10a1 1 0 0 1-1 1A9 9 0 0 1 1 2a1 1 0 0 1 1-1z"/></svg>555-014-2290</li>
      <li><svg viewBox="0 0 12 12"><path d="M1 2.5h10v7H1z M1 2.5l5 4 5-4" /></svg>dana@talentforge.com</li>
      <li><svg viewBox="0 0 12 12"><circle cx="6" cy="6" r="5.5"/></svg>www.talentforge.com</li>
    </ul>
  </section>

  <section class="card card-back" aria-label="Card back">
    <div class="brand">
      <span class="brand-dot"></span>
      <span class="brand-name">Talent Forge</span>
    </div>
    <ul class="todo-lines">
      <li></li><li></li><li></li><li></li><li></li>
    </ul>
  </section>
</body>
</html>
```